Financial Planning business needs a new Business Card design

We need a business card design for an Australian financial planning business. I am looking for a clean simple design

Target Market(s)

People aged 25-40

Industry/Entity Type

Financial Service

Contact Information for Business Card

On the front of the card we need the following information:
Name: Colin Merrow (First Name Green: #006838 and last name Grey: #414042)
Position: Financial Adviser
Qualifications: BEc(Hons), AdDipFS(FP), Dip FMBM, CFL®
Mobile: 0437 512 604
Email: colin@brightledgeplan.com.au

On the back of the card we need:
Postal address: PO BOX 5307, PERTH BC, WA 6849
Website: www.brightledgeplan.com.au
Text: AFS Licence No. 518760

The fields need to be able to be edited.

Font styles to use
Sans Serif

Requirements
Must have
• Information listed above

```html
<!DOCTYPE html>
<html lang="en">
<head>
<meta charset="utf-8">
<title>Brightledge – Business Card</title>
<link rel="stylesheet" href="https://fonts.googleapis.com/css2?family=Open+Sans:wght@400;600;700;800&display=swap">
<style>
  :root {
    --stage: #e7e5e2;
    --card-light: #fbfbfa;
    --card-dark: #1c1c1c;
    --green: #006838;
    --grey: #414042;
    --white: #ffffff;
    --rule-soft: #d0d0d0;
  }
  * { box-sizing: border-box; margin: 0; padding: 0; }
  html, body {
    width: 1200px; height: 844px; overflow: hidden;
    background: var(--stage);
    font-family: "Open Sans", Arial, sans-serif;
  }
  .stage {
    position: relative; width: 1200px; height: 844px;
    display: flex; align-items: center; justify-content: center; gap: 60px;
  }
  .card {
    position: relative; width: 510px; height: 292px;
    box-shadow: 0 10px 24px rgba(0,0,0,.22);
    overflow: hidden;
  }
  .card--front { background: var(--card-light); color: var(--grey); }
  .card--back { background: var(--card-dark); color: var(--white); }

  .brand {
    position: absolute; top: 46px; right: 34px;
    display: flex; align-items: center; gap: 10px;
    font-weight: 800; font-size: 38px; letter-spacing: -0.5px; line-height: 1;
  }
  .brand__dot { width: 12px; height: 12px; border-radius: 50%; }
  .card--front .brand { color: var(--green); }
  .card--front .brand__dot { background: var(--green); }
  .card--back .brand { color: var(--white); }
  .card--back .brand__dot { background: var(--white); }

  .rule { position: absolute; left: 0; right: 0; height: 2px; }
  .card--front .rule--main { top: 126px; background: var(--green); }
  .card--front .rule--contact { top: 218px; height: 1px; background: var(--green); left: 24px; right: 0; }
  .card--back .rule--main { top: 126px; background: var(--white); height: 1.5px; }
  .card--back .rule--web { top: 206px; height: 1px; background: var(--white); opacity: .8; left: 24px; }

  .person { position: absolute; left: 26px; top: 144px; font-size: 13.5px; line-height: 1.3; }
  .person__name { font-size: 17px; font-weight: 700; color: var(--grey); }
  .person__first { color: var(--green); }
  .person__role, .person__quals { color: var(--grey); }

  .contact { position: absolute; left: 26px; top: 226px; font-size: 14px; line-height: 1.6; list-style: none; }
  .contact__item { display: flex; align-items: center; gap: 10px; }
  .contact__icon { width: 12px; height: 12px; fill: var(--green); }

  .postal { position: absolute; left: 26px; top: 144px; font-size: 13px; line-height: 1.4; }
  .postal__label { font-weight: 700; font-size: 14px; }
  .web { position: absolute; left: 26px; top: 216px; font-size: 13px; line-height: 1.7; }
  .web__licence { font-weight: 700; }
</style>
</head>
<body>
<main class="stage">
  <section class="card card--front" aria-label="Card front">
    <div class="brand"><span class="brand__dot"></span><span class="brand__name">BRIGHTLEDGE</span></div>
    <div class="rule rule--main"></div>
    <div class="person">
      <p class="person__name"><span class="person__first">Colin</span> Merrow</p>
      <p class="person__role">Financial Adviser</p>
      <p class="person__quals">BEc(Hons), AdDipFS(FP), Dip FMBM, CFL<sup>®</sup></p>
    </div>
    <div class="rule rule--contact"></div>
    <ul class="contact">
      <li class="contact__item">
        <svg class="contact__icon" viewBox="0 0 24 24" aria-hidden="true"><path d="M6.6 10.8a15.1 15.1 0 0 0 6.6 6.6l2.2-2.2c.3-.3.7-.4 1-.2 1.1.4 2.3.6 3.6.6.6 0 1 .4 1 1V20c0 .6-.4 1-1 1A17 17 0 0 1 3 4c0-.6.4-1 1-1h3.5c.6 0 1 .4 1 1 0 1.3.2 2.5.6 3.6.1.3 0 .7-.2 1z"/></svg>
        <span>0437 512 604</span>
      </li>
      <li class="contact__item">
        <svg class="contact__icon" viewBox="0 0 24 24" aria-hidden="true"><path d="M2 5h20v14H2z M2 5l10 8 10-8" stroke="var(--card-light)" stroke-width="1.5"/></svg>
        <span>colin@brightledgeplan.com.au</span>
      </li>
    </ul>
  </section>

  <section class="card card--back" aria-label="Card back">
    <div class="brand"><span class="brand__dot"></span><span class="brand__name">BRIGHTLEDGE</span></div>
    <div class="rule rule--main"></div>
    <div class="postal">
      <p class="postal__label">Postal address</p>
      <p class="postal__value">PO BOX 5307, PERTH BC, WA 6849</p>
    </div>
    <div class="rule rule--web"></div>
    <div class="web">
      <p class="web__site">W: www.brightledgeplan.com.au</p>
      <p class="web__licence">AFS Licence No. 518760</p>
    </div>
  </section>
</main>
</body>
</html>
```